Cosmetic Label Design for a Sunless Tanner

We need a label for a new sunless tanner. The label dye will be 2.5 inches in height by 6 inches in width. It will be laser printed by Brintova.net The label will be printed on gloss laminated white polypropylene self-adhesive material. A full project description can be found in the attached Word file. The label copy is also included in a Word file.

Target Market(s)

Females aged 18 to 35

Font styles to use
Serif

Colors

Designer to choose colors to be used in the design.

Requirements
Must have
• Clean look. Strong brand image.
Nice to have
• This is the first product in a future line. The design should have the ability to move to other products.
Should not have
• Too heavy. More than 4 colors. Fonts that are whimsical. Cursive writing. No cartoon like illustrations.

```html
<!DOCTYPE html>
<html lang="en">
<head>
<meta charset="utf-8">
<title>Radiant Bronzelle – Skin Nourishing Sunless Tanner Label</title>
<link href="https://fonts.googleapis.com/css2?family=Josefin+Sans:wght@300&family=Raleway:wght@400;600&display=swap" rel="stylesheet">
<style>
  :root {
    --backdrop: #3a3a3c;
    --magenta: #c4296f;
    --magenta-light: #d83d84;
    --magenta-deep: #a11f5c;
    --ink: #ffffff;
  }
  html, body {
    margin: 0;
    padding: 0;
    width: 1200px;
    height: 554px;
    overflow: hidden;
    background: var(--backdrop);
  }
  .canvas {
    position: relative;
    width: 1200px;
    height: 554px;
    background: var(--backdrop);
  }
  .label {
    position: absolute;
    left: 32px;
    top: 30px;
    width: 1136px;
    height: 498px;
    display: flex;
    color: var(--ink);
    font-family: "Raleway", sans-serif;
  }
  .panel {
    position: relative;
    height: 100%;
    background:
      radial-gradient(circle at 18% 30%, rgba(255,255,255,0.07) 0 60px, transparent 90px),
      radial-gradient(circle at 70% 72%, rgba(255,255,255,0.06) 0 70px, transparent 110px),
      radial-gradient(circle at 85% 18%, rgba(0,0,0,0.06) 0 50px, transparent 90px),
      radial-gradient(ellipse at 40% 90%, var(--magenta-light), transparent 60%),
      var(--magenta);
  }
  .panel--info { width: 406px; }
  .panel--front {
    width: 323px;
    background:
      radial-gradient(circle at 30% 20%, rgba(255,255,255,0.06) 0 50px, transparent 90px),
      radial-gradient(circle at 75% 80%, rgba(255,255,255,0.05) 0 60px, transparent 100px),
      var(--magenta-deep);
    text-align: center;
  }
  .panel--ingredients { width: 407px; }

  /* Info panel */
  .info {
    position: absolute;
    left: 45px;
    top: 86px;
    width: 313px;
    font-size: 9.6px;
    line-height: 12.2px;
  }
  .info p { margin: 0; text-align: justify; }
  .info h3 {
    margin: 10px 0 6px 6px;
    font-size: 9.6px;
    font-weight: 600;
  }
  .info ul {
    list-style: none;
    margin: 0;
    padding: 0;
  }
  .info li {
    position: relative;
    padding-left: 6px;
  }
  .info li::before {
    content: "•";
    position: absolute;
    left: 0;
  }
  .info .warning { margin-left: 6px; text-align: left; }

  /* Front panel */
  .seal {
    position: absolute;
    left: 50%;
    top: 82px;
    transform: translateX(-50%);
  }
  .brand {
    position: absolute;
    left: 0;
    right: 0;
    top: 176px;
    font-family: "Josefin Sans", sans-serif;
    font-weight: 300;
    margin: 0;
    line-height: 1;
  }
  .brand__first { display: block; font-size: 42px; }
  .brand__last { display: block; font-size: 47px; margin-top: 14px; letter-spacing: 1px; }
  .rule {
    position: absolute;
    left: 18px;
    width: 287px;
    top: 312px;
    height: 2px;
    background: var(--ink);
  }
  .product {
    position: absolute;
    left: 0;
    right: 0;
    top: 354px;
    margin: 0;
    font-family: "Josefin Sans", sans-serif;
    font-weight: 300;
    font-size: 35px;
    line-height: 38px;
  }

  /* Ingredients panel */
  .ingredients {
    position: absolute;
    left: 50px;
    top: 142px;
    width: 314px;
    font-size: 9.6px;
    line-height: 12.2px;
  }
  .ingredients h3 {
    margin: 0 0 10px;
    font-size: 9.6px;
    font-weight: 600;
  }
  .ingredients p { margin: 0; text-align: justify; }
  .maker {
    margin-top: 20px !important;
    text-align: left !important;
  }
  .maker strong { font-weight: 600; }
</style>
</head>
<body>
<div class="canvas">
  <div class="label">
    <section class="panel panel--info">
      <div class="info">
        <p>Need a tan fast? Scared of harmful effects from the sun? We've got your back! Made from the highest quality natural ingredients, Radiant Bronzelle Skin Nourishing Sunless Tanner creates a medium golden tan while providing silky-soft, color enhancing moisture to your skin.</p>
        <h3>Directions for use:</h3>
        <ul>
          <li>Cleanse and exfoliate skin</li>
          <li>Apply your favorite moisturizer to dryer areas like knees, elbows, ankles,and wrists</li>
          <li>Smooth a generous amount of product anywhere you'd like to tan</li>
          <li>Massage into skin</li>
          <li>Kick back and relax a minute, allowing product to dry</li>
          <li>Wash hands thoroughly with soap and water after application</li>
          <li>Watch your skin begin to glow as your tan develops over the next several hours</li>
        </ul>
        <h3>For best results:</h3>
        <ul>
          <li>Allow the tanner to stay on your skin for several hours before showering or swimming</li>
          <li>For an even darker look, repeat the application process for two or more days in a row</li>
          <li>Reapply as needed to achieve the results you desire</li>
        </ul>
        <h3>Warning:</h3>
        <p class="warning">For external use only. Does not contain sunscreen and does not protect against sunburn.</p>
      </div>
    </section>

    <section class="panel panel--front">
      <svg class="seal" width="44" height="44" viewBox="0 0 44 44" aria-hidden="true">
        <circle cx="22" cy="22" r="21" fill="#ffffff"/>
      </svg>
      <h1 class="brand">
        <span class="brand__first">Radiant</span>
        <span class="brand__last">BRONZELLE</span>
      </h1>
      <div class="rule"></div>
      <h2 class="product">Skin Nourishing<br>Sunless Tanner</h2>
    </section>

    <section class="panel panel--ingredients">
      <div class="ingredients">
        <h3>Ingredient List</h3>
        <p>Water, Aloe Barbadensis Gel, Glycine Soja (Soybean) Oil,Dihydroxyacetone, Caramel, Caprylic/Capric Triglyceride, Citrus Reticulata (Mandarin Orange) Oil, Argania Spinosa (Argan) Oil, Retinyl Palmitate &amp; Ascorbyl Palmitate &amp; Tocopheryl Acetate, Saccharomyces Magnesium Ferment, Hydrolysate Saccharomyces Potassium Ferment Hydrolysate, Adenosine Triphosphate, Palmitoyl Oligopeptide &amp; Palmitoyl Tetrapeptide-7 &amp; Glycerin &amp; Butylene Glycol &amp; Carbomer &amp; Polysorbate 20, Olea Europaea (Olive) Oil, Triticum Aestivum (Wheat) Peptide, Avena Sativa (Oat) Oil, Glycince Soja (Soy) Peptide, Yeast Extract, Cupric Sulfate, Zinc Sulfate, Bana Fruit Extract, Juglans Regia (Walnut) Extract, Hydrolized Collagen, Tyrosine, Panthenol, Polyacrylamide &amp; C13-14 Isoparaffin &amp; Laureth-7, Phenoxyethanol Dimethicone, D&amp;C Red 33 (CI 17200)</p>
        <p class="maker">Never tested on animals<br>Manufactured for Radiant Bronzelle L.L.C in the USA<br><strong>radiantbronzelle.com</strong><br>Fairhaven, NC&nbsp; 27000</p>
      </div>
    </section>
  </div>
</div>
</body>
</html>
```